I'm looking for a fresh new design for my business Leonard Fasque Creative.
I am a photographer and videographer.
The card must be easy to print, eye catching and easy to read. It must reflect the fact that I work in a creative area, but not so edgy as to scare away my corporate clients.
Sub text should read Photography, Video, Design
There also needs to be room for phone number and email.

```html
<!DOCTYPE html>
<html lang="en">
<head>
<meta charset="utf-8">
<title>Leonard Fasque Creative – Business Card</title>
<link href="https://fonts.googleapis.com/css2?family=Jost:wght@400;500;700&display=swap" rel="stylesheet">
<style>
  :root {
    --stage: #e9ecef;
    --card-white: #fbfbfb;
    --card-blue: #4cb9e9;
    --accent-blue: #3aa9dc;
    --ink-dark: #3a3a3c;
    --ink-grey: #6e6e70;
    --white: #ffffff;
  }
  * { margin: 0; padding: 0; box-sizing: border-box; }
  html, body {
    width: 1200px;
    height: 676px;
    overflow: hidden;
    background: var(--stage);
    font-family: "Jost", "Futura", sans-serif;
  }
  .stage {
    width: 1200px;
    height: 676px;
    display: flex;
    align-items: center;
    justify-content: center;
    gap: 60px;
  }
  .card {
    position: relative;
    width: 500px;
    height: 286px;
    border-radius: 3px;
    box-shadow: 0 6px 18px rgba(0, 0, 0, 0.12);
    overflow: hidden;
  }

  /* Front */
  .card--front { background: var(--card-white); }
  .brand {
    position: absolute;
    top: 34px;
    right: 34px;
    text-align: right;
  }
  .brand__name {
    font-weight: 700;
    font-size: 30px;
    line-height: 1;
    letter-spacing: 0.5px;
    color: var(--ink-dark);
    text-transform: uppercase;
  }
  .brand__sub {
    font-weight: 400;
    font-size: 16px;
    letter-spacing: 4px;
    color: var(--ink-dark);
    text-transform: uppercase;
    margin-top: 4px;
  }
  .services {
    margin-top: 6px;
    font-size: 14px;
    color: var(--ink-grey);
    display: flex;
    justify-content: flex-end;
    align-items: center;
    gap: 5px;
  }
  .services svg { width: 7px; height: 8px; fill: var(--accent-blue); }

  .contact {
    position: absolute;
    left: 36px;
    bottom: 32px;
  }
  .contact__name {
    font-size: 20px;
    font-weight: 400;
    color: var(--accent-blue);
    margin-bottom: 10px;
  }
  .contact__list { list-style: none; }
  .contact__item {
    display: flex;
    align-items: center;
    gap: 10px;
    font-size: 14.5px;
    line-height: 22px;
    color: var(--ink-dark);
  }
  .contact__item svg {
    width: 12px;
    height: 12px;
    fill: none;
    stroke: var(--accent-blue);
    stroke-width: 1.6;
    flex-shrink: 0;
  }

  /* Back */
  .card--back {
    background: var(--card-blue);
    display: flex;
    flex-direction: column;
    justify-content: center;
    padding-left: 44px;
  }
  .back__name {
    font-weight: 700;
    font-size: 36px;
    line-height: 1;
    color: var(--white);
    text-transform: uppercase;
    letter-spacing: 0.5px;
  }
  .back__sub {
    font-weight: 700;
    font-size: 36px;
    line-height: 1.1;
    color: var(--white);
    text-transform: uppercase;
    letter-spacing: 0.5px;
  }
  .back__web {
    margin-top: 10px;
    font-size: 18px;
    color: var(--white);
  }
</style>
</head>
<body>
<main class="stage">

  <section class="card card--front" aria-label="Card front">
    <div class="brand">
      <div class="brand__name">Leonard Fasque</div>
      <div class="brand__sub">Creative</div>
      <div class="services">
        <span>Photography</span>
        <svg viewBox="0 0 7 8"><polygon points="0,0 7,4 0,8"/></svg>
        <span>Video</span>
        <svg viewBox="0 0 7 8"><polygon points="7,0 0,4 7,8"/></svg>
        <span>Design</span>
      </div>
    </div>

    <div class="contact">
      <div class="contact__name">Leonard Fasque</div>
      <ul class="contact__list">
        <li class="contact__item">
          <svg viewBox="0 0 12 12"><path d="M2 1.5 L4 1.5 L5 4 L3.8 5 Q5 7.5 7 8.2 L8 7 L10.5 8 L10.5 10 Q5 11 1.5 4 Z"/></svg>
          555.0142.718
        </li>
        <li class="contact__item">
          <svg viewBox="0 0 12 12"><rect x="3" y="1" width="6" height="10" rx="1"/><line x1="5" y1="9.2" x2="7" y2="9.2"/></svg>
          555.0142.718
        </li>
        <li class="contact__item">
          <svg viewBox="0 0 12 12"><rect x="1" y="2.5" width="10" height="7"/><polyline points="1,2.5 6,6.5 11,2.5"/></svg>
          info@leonardfasque.com
        </li>
        <li class="contact__item">
          <svg viewBox="0 0 12 12"><circle cx="6" cy="6" r="5"/><ellipse cx="6" cy="6" rx="2.2" ry="5"/><line x1="1" y1="6" x2="11" y2="6"/></svg>
          www.leonardfasque.com
        </li>
      </ul>
    </div>
  </section>

  <section class="card card--back" aria-label="Card back">
    <div class="back__name">Leonard Fasque</div>
    <div class="back__sub">Creative</div>
    <div class="back__web">leonardfasque.com</div>
  </section>

</main>
</body>
</html>
```